Tanner's Goat sports bar beer & food menu

We need a menu design for our gastropub sports bar in L.A.'s Marlowe Quarter (Little Nara). We have a full-bar (hard liquor, craft beer, wine and cocktails) . We have a lunch and dinner menu as well as a happy hour menu. On Sundays we have a seperate menu with brunch items. The design concept is a British pub type of sports bar. We're looking for something different from our existing menu design. Ideally something cleaner and more legible. It should mesh a simple, modern sensibility with the more traditional darkened pub style of our interior design.

You can check out our Chirpa page for photos of the interior/exterior:
https://www.chirpa-reviews.example/biz_photos/tanners-goat-los-angeles?tab=interior

You can view our existing menu here:
https://www.chirpa-reviews.example/biz_photos/tanners-goat-los-angeles?tab=menu

If there's an area of the design that can be a little more playful it's our highlighted event schedule so that the events will stand out.

Target Market(s)

Age of 25 and up. Marlowe is a cultural hub that caters to a younger, moderately affluent crowd.

Industry/Entity Type

Sports Bar

Font styles to use
Sans Serif

Colors

Designer to choose colors to be used in the design.

Requirements
Must have
• Logo, highlighted event schedule (beer pong Monday, trivia Tuesday, taco Tuesday, whiskey Wednesday, karaoke Saturday). The menu should be easy to read in a darkened bar. We'll be printing on standard 8.5x11 in portrait.
Nice to have
• We're trying to have the menu take up as few pages as possible.
Should not have
• We're trying to have the menu take up as few pages as possible. Food photography isn't necessary. A cover isn't necessary. Please avoid clip art of food.

```html
<!DOCTYPE html>
<html lang="en">
<head>
<meta charset="utf-8">
<title>Tanner's Goat — Menu</title>
<link rel="stylesheet" href="https://fonts.googleapis.com/css2?family=Oswald:wght@500&family=Roboto+Condensed:wght@400;700&display=swap">
<style>
:root{
  --paper:#f7f6f2;
  --ink:#1b1b1b;
  --edge:#2a2a2a;
  --amber:#f2a823;
  --amber-soft:#fbe7bf;
  --amber-text:#2b2210;
}
*{margin:0;padding:0;box-sizing:border-box}
html,body{width:941px;height:1200px;overflow:hidden;background:var(--paper)}
.menu{position:relative;width:941px;height:1200px;background:var(--paper);color:var(--ink);font-family:"Roboto Condensed",Arial,sans-serif}
.menu__edge{position:absolute;left:0;right:0;height:5px;background:var(--edge)}
.menu__edge--top{top:0}
.menu__edge--bottom{bottom:0}

.brand{position:absolute;top:96px;left:0;right:0;text-align:center}
.brand__mark{display:inline-block;width:30px;height:30px;border-radius:50%;background:var(--amber);margin-bottom:10px}
.brand__name{font-weight:700;font-size:44px;line-height:1;color:var(--ink);letter-spacing:.5px}
.brand__tagline{margin-top:8px;font-size:11px;letter-spacing:4px;text-transform:uppercase}

.column{position:absolute;top:308px;width:380px}
.column--left{left:68px}
.column--right{left:488px}

.section__title{background:var(--amber);color:var(--amber-text);font-family:"Oswald",Arial,sans-serif;font-weight:500;font-size:12.5px;letter-spacing:1px;text-transform:uppercase;height:18px;line-height:18px;padding-left:4px;margin-bottom:22px}
.section + .section{margin-top:36px}

.item{display:flex;justify-content:space-between;align-items:flex-start;margin-bottom:18px}
.item__text{width:320px}
.item__name{font-weight:700;font-size:13.5px;line-height:17px}
.item__desc{font-size:13.5px;line-height:17px}
.item__price{font-size:13.5px;line-height:17px;text-align:right}
.item--price-low .item__price{padding-top:17px}

.events{position:absolute;top:1036px;left:68px;width:805px}
.events .section__title{margin-bottom:14px}
.events__list{display:flex;gap:10px;list-style:none}
.event{flex:1;background:var(--amber-soft);border-left:4px solid var(--amber);padding:8px 10px;height:52px}
.event__day{font-family:"Oswald",Arial,sans-serif;font-weight:500;font-size:11.5px;letter-spacing:1px;text-transform:uppercase}
.event__name{font-weight:700;font-size:14px;line-height:18px;margin-top:2px}
.bar-note{margin-top:14px;font-size:13.5px;line-height:17px;text-align:center}
.bar-note__label{font-weight:700}
</style>
</head>
<body>
<main class="menu">
  <div class="menu__edge menu__edge--top"></div>

  <header class="brand">
    <span class="brand__mark"></span>
    <div class="brand__name">Tanner's Goat</div>
    <div class="brand__tagline">Pub &amp; Restaurant</div>
  </header>

  <div class="column column--left">
    <section class="section">
      <h2 class="section__title">Burgers and Sandwiches</h2>
      <div class="item"><div class="item__text"><div class="item__name">Chicken Sandwich</div><div class="item__desc">Chicken Breast, Applewood Bacon, Butter Lettuce, White Cheddar, Avocado and Tomato Served on Sourdough Bread</div></div><div class="item__price">$12</div></div>
      <div class="item"><div class="item__text"><div class="item__name">Buttermilk Fried Chicken</div><div class="item__desc">Coleslaw, Provolone, Tomato, and a Spiced Mayonnaise on a Pretzel Roll</div></div><div class="item__price">$13</div></div>
      <div class="item"><div class="item__text"><div class="item__name">Short Rib Sandwich</div><div class="item__desc">Beef Shorts, Mayo, Tomato, Caramelized Onions, Arugula, Pepper Jack Cheese (Served on Sourdough Bread)</div></div><div class="item__price">$13</div></div>
      <div class="item item--price-low"><div class="item__text"><div class="item__name">Grilled Cheese Sandwich</div><div class="item__desc">Cheese, Provolone and Cheddar Cheese</div></div><div class="item__price">$10</div></div>
      <div class="item item--price-low"><div class="item__text"><div class="item__name">Tanner's Goat Burger</div><div class="item__desc">Sharp Cheddar, Arugula, Roasted Shallots, Bacon Jam with Malt Aioli</div></div><div class="item__price">$14</div></div>
      <div class="item item--price-low"><div class="item__text"><div class="item__name">The Truffle Burger</div><div class="item__desc">Caramelized Onions, Arugula, Truffle Pecorino, Truffle Mayo and Truffle Fries</div></div><div class="item__price">$15</div></div>
      <div class="item item--price-low"><div class="item__text"><div class="item__name">The Sloppy Joe.</div><div class="item__desc">Shredded Lettuce and Sharp Cheddar</div></div><div class="item__price">$10</div></div>
      <div class="item item--price-low"><div class="item__text"><div class="item__name">Veggie Burger</div><div class="item__desc">Concoction of kale, Tomato, Avocado, Sharp Cheddar with a Balsamic Reduction</div></div><div class="item__price">$12</div></div>
      <div class="item item--price-low"><div class="item__text"><div class="item__name">Flat Iron Steak Sandwich</div><div class="item__desc">Arugula, Peppers, Fontina, Onion and Mayo</div></div><div class="item__price">$16</div></div>
      <div class="item item--price-low"><div class="item__text" style="width:300px"><div class="item__name">Chicken Spinach Wrap</div><div class="item__desc">Chicken, Bacon, Lettuce, Tomato, Avocado, Ranch and Mayo</div></div><div class="item__price">$20</div></div>
      <div class="item item--price-low"><div class="item__text"><div class="item__name">Fried Chicken Sliders (4)</div><div class="item__desc">Coleslaw, Lime Sriracha Sauce</div></div><div class="item__price">$12</div></div>
    </section>
  </div>

  <div class="column column--right">
    <section class="section">
      <h2 class="section__title">Big Dog Bites</h2>
      <div class="item"><div class="item__text"><div class="item__name">Atlantic Cod Fish N' Chips...$15</div><div class="item__desc">House Tartar Sauce, Vinegar and Lemon Wedge</div></div><div class="item__price">$15</div></div>
      <div class="item"><div class="item__text"><div class="item__name">Oven Roasted ½ Roasted Chicken...$16</div><div class="item__desc">Boneless Chicken, Broccolini, Fingerling Potatoes, Topped with Chimichurri Sauce</div></div><div class="item__price">$16</div></div>
      <div class="item"><div class="item__text"><div class="item__name">Black Mussels...$17</div><div class="item__desc">Tequila Chipotle Sauce, Cilantro and Cherry Tomatoes</div></div><div class="item__price">$17</div></div>
      <div class="item"><div class="item__text"><div class="item__name">Pan Seared Salmon...$19</div><div class="item__desc">Sushi Grade Salmon, Spaghetti Squash, Zucchini, Cherry Tomatoes (In a Lemon Caper Beurre Blanc)</div></div><div class="item__price">$19</div></div>
      <div class="item"><div class="item__text"><div class="item__name">Flat Iron Steak...$22</div><div class="item__desc">French Fries, Baby Arugula in a Light peppercorn Sauce</div></div><div class="item__price">$22</div></div>
    </section>

    <section class="section">
      <h2 class="section__title">Burgers and Sandwiches</h2>
      <div class="item"><div class="item__text"><div class="item__name">Margherita</div><div class="item__desc">Fresh Mozzarella, Roma Tomatoes and Fresh Italian Basil</div></div><div class="item__price">$12</div></div>
      <div class="item"><div class="item__text"><div class="item__name">Vegetarian</div><div class="item__desc">Brussel Sprouts, Peppers, Onions, Zucchini, Goat Cheese, Smoked Mozzarella (Topped with a Balsamic Reduction)</div></div><div class="item__price">$13</div></div>
      <div class="item"><div class="item__text"><div class="item__name">Prosciutto &amp; Arugula</div><div class="item__desc">Red Onion, Parmesan, Mozzarella</div></div><div class="item__price">$14</div></div>
      <div class="item"><div class="item__text" style="width:300px"><div class="item__name">Portobello &amp; Truffle</div><div class="item__desc">Portobello White Mushroom, Fontina, Drizzled with Truffle Oil</div></div><div class="item__price">$14</div></div>
      <div class="item"><div class="item__text"><div class="item__name">Chicken Tikka Masala</div><div class="item__desc">Tandoori Chicken, Fontini and Raita</div></div><div class="item__price">$14</div></div>
      <div class="item"><div class="item__text"><div class="item__name">The Tanner's Goat</div><div class="item__desc">Meatballs, Sausage, Chorizo, Mozzarella and Fresen</div></div><div class="item__price">$15</div></div>
    </section>
  </div>

  <section class="events">
    <h2 class="section__title">Weekly Events</h2>
    <ul class="events__list">
      <li class="event"><div class="event__day">Monday</div><div class="event__name">Beer Pong</div></li>
      <li class="event"><div class="event__day">Tuesday</div><div class="event__name">Trivia Tuesday</div></li>
      <li class="event"><div class="event__day">Tuesday</div><div class="event__name">Taco Tuesday</div></li>
      <li class="event"><div class="event__day">Wednesday</div><div class="event__name">Whiskey Wednesday</div></li>
      <li class="event"><div class="event__day">Saturday</div><div class="event__name">Karaoke</div></li>
    </ul>
    <p class="bar-note"><span class="bar-note__label">Full Bar:</span> Hard Liquor · Craft Beer · Wine · Cocktails</p>
  </section>

  <div class="menu__edge menu__edge--bottom"></div>
</main>
</body>
</html>
```